bizcards, stationary, envelopes, powerpoint template, invoice template, polo shirts, email template
ms word templates of stationary also please
bizcards, stationary, envelopes,  powerpoint template, invoice template, polo shirts, email template - Aviation
Creative Brief
Professional
Samuel K Orlowski
Founder
The Halvern Tower 482 Tamsin Ridge Rd. Suite 210 Carrowfield, OH 44718
sorlowski@meridowair.example
www.meridowair.example
Air Carrier #4RXB519T
Only use the colors and font of our logo. Our tag line "YOUR SKY, YOUR HOUR" can be used in a creative way of your thoughts.
wide ope, maybe a Skyvalent Jet watermark, the tag line, the tag line & logo, etc.

```html
<!DOCTYPE html>
<html lang="en">
<head>
<meta charset="utf-8">
<title>Meridow Air Charter – Business Card</title>
<link rel="stylesheet" href="https://fonts.googleapis.com/css2?family=Montserrat:ital,wght@0,400;0,600;1,800&family=Open+Sans:wght@400;600&display=swap">
<style>
  :root{
    --bg:#ece9e4;
    --card:#ffffff;
    --green:#7dc242;
    --green-dark:#5fa52e;
    --grey:#6d6e71;
    --grey-dark:#58595b;
    --text:#4a4a4a;
    --jet-light:#f1f3f4;
    --jet-mid:#d9dde0;
  }
  *{box-sizing:border-box;margin:0;padding:0}
  html,body{width:1200px;height:506px;overflow:hidden;background:var(--bg)}
  .canvas{position:relative;width:1200px;height:506px}
  .card{position:absolute;top:108px;width:540px;height:276px;background:var(--card);
        box-shadow:0 2px 6px rgba(0,0,0,.18);overflow:hidden}
  .card--front{left:42px}
  .card--back{left:616px}

  .brand{position:absolute;font-family:"Montserrat",sans-serif;font-weight:600;
         color:var(--grey-dark);white-space:nowrap}
  .card--front .brand{left:60px;top:40px;font-size:26px}
  .card--back .brand{left:32px;top:30px;font-size:20px}

  .holder{position:absolute;left:0;right:0;top:112px;text-align:center;
          font-family:"Open Sans",sans-serif;font-size:15px;color:var(--text)}
  .holder__divider{color:var(--green);margin:0 4px}
  .holder__role{color:var(--green)}

  .contact{position:absolute;left:60px;top:150px;list-style:none;
           font-family:"Open Sans",sans-serif;font-size:9.5px;color:var(--text)}
  .contact li{display:flex;align-items:center;gap:7px;height:15px}
  .contact__icon{width:10px;height:10px;background:var(--green);display:inline-flex;
                 align-items:center;justify-content:center;color:#fff;font-size:7px;font-weight:600}

  .address{position:absolute;left:232px;top:150px;font-family:"Open Sans",sans-serif;
           font-style:normal;font-size:9.5px;line-height:13px;color:var(--text)}
  .address__licence{margin-top:12px}

  .swoosh{position:absolute;bottom:0}
  .card--front .swoosh{right:0}
  .card--back .swoosh{left:0}

  .jet{position:absolute;left:150px;top:30px;width:390px;height:180px;
       background:radial-gradient(ellipse at 55% 55%,var(--jet-mid) 0%,var(--jet-light) 55%,rgba(255,255,255,0) 75%)}
  .tagline{position:absolute;right:22px;bottom:26px;font-family:"Montserrat",sans-serif;
           font-style:italic;font-weight:800;font-size:21px;color:var(--green);letter-spacing:.5px}
  .tagline__accent{color:var(--grey-dark);font-size:25px}
</style>
</head>
<body>
<main class="canvas">
  <section class="card card--front">
    <p class="brand">Meridow Air Charter</p>
    <p class="holder">Samuel K Orlowski<span class="holder__divider">|</span><span class="holder__role">Founder</span></p>
    <ul class="contact">
      <li><span class="contact__icon">T</span>877-555-0142</li>
      <li><span class="contact__icon">O</span>440-555-0187</li>
      <li><span class="contact__icon">C</span>716-555-0163</li>
      <li><span class="contact__icon">F</span>440-555-0129</li>
      <li><span class="contact__icon">E</span>sorlowski@meridowair.example</li>
      <li><span class="contact__icon">W</span>www.meridowair.example</li>
    </ul>
    <address class="address">
      The Halvern Tower<br>482 Tamsin Ridge Rd.<br>Suite 210<br>Carrowfield, OH 44718
      <p class="address__licence">License No., if any<br>Air Carrier #4RXB519T</p>
    </address>
    <svg class="swoosh" width="200" height="60" viewBox="0 0 200 60" aria-hidden="true">
      <path d="M200 8 C150 40 80 55 0 60 L200 60 Z" fill="var(--green)"/>
      <path d="M200 20 C150 46 90 56 30 60 L200 60 Z" fill="var(--green-dark)"/>
    </svg>
  </section>

  <section class="card card--back">
    <div class="jet" role="img" aria-label="Faint illustration of a private business jet in flight"></div>
    <p class="brand">Meridow Air Charter</p>
    <svg class="swoosh" width="200" height="40" viewBox="0 0 200 40" aria-hidden="true">
      <path d="M0 30 C60 20 140 26 200 40 L0 40 Z" fill="var(--green)"/>
    </svg>
    <p class="tagline">YOUR <span class="tagline__accent">SKY,</span> YOUR HOUR</p>
  </section>
</main>
</body>
</html>
```